quillfernPRESS is launching 2 new eBooks and needs beautiful and compelling cover designs and a desig

We are launching 2 non-fiction eBooks that are part of a series but will be launched separately, so we would like to see some continuity between the 2 designs - but each should have a strong stand alone identity.

The eBooks are both in the naturopathic/holistic health niche.

ebook 1 title is:
Shaping A Thriving Clinic
(sub) The Holistic Guide to building your own successful natural and
alternative therapy business.

The book is a comprehensive guide for naturopaths and other alternative health providers - ( Naturopath,
Nutritionist, Homeopath, Acupuncturist, Chiropractor,
Massage Therapist, or Holistic Health Specialist), who are seeking to setup their own, profitable naturopathic business.

ebook 2 title is:
Silver Pathways (subtitle) Get 30 + Clients in Under a Month

(sub/sub)32 ways to market your natural and alternative therapy business

This book is a list of 32 tips for the same audience to increase there customer referrals (and therefore income).

Each book should feature
written by Carla Whitmore
published by Whitmore Publishing

Each book should feature the authors photograph on the cover (attached) - no caveats on cropping etc - whatever fits with the design.

You can see more about the writer on her website here:

http://www.lakemeadowwellness.example.au/

What we require:

1) cover art for both eBooks that conforms to Kindle and iPad specs
2) Flat & 3D book cover art for use on website and marketing campaigns
3) we will require layered PSD files on completion of project.

I'd like to add that we are seeking to build a relationship with the designer we choose for this project, as we are publishing many other titles throughout 2014

Many eBook writers jump straight to Gigly for a cover. The result is most self published books have the same generic look the 'gigly' look.

I don't want that look.

We want to reward great design and ensure quillfernPRESS eBook titles have a great look.

The winning designer will be working with us on many more projects.

Martin Oakes
quillfernPRESS

```html
<!DOCTYPE html>
<html lang="en">
<head>
<meta charset="utf-8">
<title>Shaping A Thriving Clinic — Carla Whitmore</title>
<link rel="stylesheet" href="https://fonts.googleapis.com/css2?family=Josefin+Sans:wght@400&family=Marcellus&display=swap">
<style>
  :root {
    --backdrop: #5ba01f;
    --paper: #ffffff;
    --title-green: #243b2e;
    --accent-orange: #f7921e;
    --band-text: #ffffff;
    --sunlight: #fbf6c4;
    --canopy-light: #cfe07a;
    --canopy-mid: #7f9e34;
    --trunk-shade: #3f5a1e;
    --grass-bright: #b9d44a;
    --grass-mid: #7fa62c;
    --grass-deep: #3f6a16;
    --portrait-light: #eef0ee;
    --portrait-tone: #d9c3ae;
    --portrait-garment: #8e3d3f;
  }
  * { box-sizing: border-box; margin: 0; padding: 0; }
  html, body {
    width: 1029px;
    height: 1200px;
    overflow: hidden;
    background: var(--backdrop);
  }
  .book-cover {
    position: absolute;
    left: 94px;
    top: 15px;
    width: 840px;
    height: 1170px;
    background: var(--paper);
    overflow: hidden;
  }
  .cover-header {
    position: absolute;
    left: 0; top: 0;
    width: 100%;
    height: 478px;
    text-align: center;
    color: var(--title-green);
  }
  .author-name {
    margin-top: 34px;
    font-family: "Josefin Sans", sans-serif;
    font-size: 44px;
    letter-spacing: 2px;
    color: var(--accent-orange);
  }
  .book-title {
    margin-top: 14px;
    font-family: "Marcellus", serif;
    font-weight: 400;
    line-height: 1;
  }
  .book-title .line-lead { display: block; font-size: 90px; letter-spacing: 6px; }
  .book-title .line-mid  { display: block; font-size: 68px; letter-spacing: 3px; margin-top: 10px; }
  .book-title .line-end  { display: block; font-size: 76px; letter-spacing: 6px; margin-top: 6px; }
  .book-subtitle {
    margin: 12px auto 0;
    font-family: "Marcellus", serif;
    font-size: 21px;
    letter-spacing: 0.6px;
    line-height: 1.14;
  }
  .accent-rule {
    position: absolute;
    left: 0; top: 478px;
    width: 100%;
    height: 8px;
    background: var(--accent-orange);
  }
  .meadow-scene {
    position: absolute;
    left: 0; top: 486px;
    width: 100%;
    height: 638px;
    background:
      radial-gradient(ellipse 260px 220px at 44% 34%, rgba(251, 246, 196, 0.95) 0%, rgba(251, 246, 196, 0.45) 45%, rgba(251, 246, 196, 0) 100%),
      radial-gradient(ellipse 420px 160px at 50% 52%, rgba(214, 232, 96, 0.7) 0%, rgba(214, 232, 96, 0) 100%),
      linear-gradient(180deg,
        var(--canopy-light) 0%,
        var(--canopy-mid) 14%,
        var(--trunk-shade) 26%,
        var(--canopy-mid) 34%,
        var(--grass-bright) 42%,
        var(--grass-mid) 62%,
        var(--grass-deep) 100%);
  }
  .author-portrait {
    position: absolute;
    left: 313px;
    top: 436px;
    width: 214px;
    height: 214px;
    border-radius: 50%;
    border: 9px solid var(--accent-orange);
    background:
      radial-gradient(ellipse 70px 110px at 50% 62%, var(--portrait-tone) 0%, var(--portrait-tone) 60%, rgba(217, 195, 174, 0) 100%),
      linear-gradient(180deg, var(--portrait-light) 0%, var(--portrait-light) 70%, var(--portrait-garment) 100%);
  }
  .publisher-band {
    position: absolute;
    left: 0; bottom: 0;
    width: 100%;
    height: 46px;
    background: var(--accent-orange);
    color: var(--band-text);
    font-family: "Marcellus", serif;
    font-size: 23px;
    line-height: 48px;
    text-align: center;
    letter-spacing: 0.5px;
  }
</style>
</head>
<body>
  <main class="book-cover">
    <header class="cover-header">
      <p class="author-name">CARLA WHITMORE</p>
      <h1 class="book-title">
        <span class="line-lead">SHAPING</span>
        <span class="line-mid">A THRIVING</span>
        <span class="line-end">CLINIC</span>
      </h1>
      <p class="book-subtitle">The Holistic Guide to building<br>your own successful natural and<br>alternative therapy business</p>
    </header>
    <div class="accent-rule"></div>
    <div class="meadow-scene" role="img" aria-label="Sunlit forest clearing: tree trunks backlit by sun rays over a bright green grassy slope"></div>
    <div class="author-portrait" role="img" aria-label="Portrait photograph of the author"></div>
    <footer class="publisher-band">Whitmore Publishing</footer>
  </main>
</body>
</html>
```